Breakfast Briefings / Lunch & Learn

I would like to have a double sided flyer size 8x10 to display the breakfast briefing on one side and Lunch & Learn on the other side.

Header on each side to say
2018 Calendar Breakfast Briefing (on the breakfast side)
2018 Calendar Lunch & Learn (on the lunch side)

I have attached a copy of the files we would like to use.

Learn

```html
<!DOCTYPE html>
<html lang="en">
<head>
<meta charset="utf-8">
<title>2018 Calendar – Breakfast Briefings / Lunch &amp; Learn</title>
<link href="https://fonts.googleapis.com/css2?family=Exo+2:wght@800;900&family=Montserrat:wght@400;500;600&display=swap" rel="stylesheet">
<style>
:root{
  --stage:#3c3c3e;
  --navy:#263f94;
  --blue-top:#2b4f9c;
  --teal-bottom:#1b8e9b;
  --header-tint:#d8dbe8;
  --orange-ring:#ef5a24;
  --white:#ffffff;
  --lunch-tint:#cfe7e6;
  --lunch-title:#4e908e;
  --lunch-band:#7db3b1;
  --lunch-sub:#d5e9e8;
  --lunch-line:#6aa9a7;
  --sunday:#e8837f;
  --ink:#3d3d3f;
  --hl:#b9bbbd;
  --orbit:#c9ccd3;
  --c-tos:#21a04b;
  --c-medical:#d0202e;
  --c-sales:#3a3b3d;
  --c-finance:#1caa9d;
  --c-rnd:#6cb33f;
  --c-ops:#ef5a24;
  --c-clinical:#cf1f2d;
  --c-quality:#58595b;
  --c-people:#1b75bc;
  --c-marketing:#9e1f63;
  --c-legal:#f7941d;
  --c-access:#8b5a2b;
}
*{margin:0;padding:0;box-sizing:border-box}
html,body{width:1200px;height:855px;overflow:hidden;background:var(--stage)}
body{position:relative;font-family:"Montserrat",sans-serif}
.page{position:absolute;top:100px;width:524px;height:655px;overflow:hidden}
.page--breakfast{left:58px;background:linear-gradient(170deg,var(--blue-top) 0%,#22709e 55%,var(--teal-bottom) 100%)}
.page--lunch{left:618px;background:var(--white)}

.header{position:absolute;top:30px;height:82px;border-radius:0 0 26px 26px;text-align:center;font-family:"Exo 2",sans-serif;font-weight:900;line-height:1}
.page--breakfast .header{left:42px;width:432px;background:var(--header-tint);color:var(--navy)}
.page--lunch .header{left:46px;width:432px;background:var(--lunch-tint);color:var(--lunch-title)}
.header__year{display:block;font-size:41px;padding-top:8px;letter-spacing:.5px}
.header__sub{display:block;font-size:27px;margin-top:2px;font-weight:800}

.orbit{position:absolute;left:0;top:0}
.hero{position:absolute;left:128px;top:236px;width:272px;height:272px;border-radius:50%;background:linear-gradient(135deg,#8a6a4a,#c9b49a 45%,#3c3c3c 60%,#a08462)}
.dept{position:absolute;width:84px;height:84px;margin:-42px 0 0 -42px;border-radius:50%;border:3px solid var(--white);box-shadow:0 3px 6px rgba(0,0,0,.35);display:flex;align-items:center;justify-content:center;text-align:center;color:var(--white);font-size:9.6px;font-weight:600;line-height:1.22;background-image:linear-gradient(180deg,rgba(255,255,255,.22),rgba(255,255,255,0) 55%)}
.dept--tos{left:192px;top:186px;background-color:var(--c-tos)}
.dept--medical{left:289px;top:178px;background-color:var(--c-medical)}
.dept--sales{left:382px;top:214px;background-color:var(--c-sales)}
.dept--finance{left:448px;top:292px;background-color:var(--c-finance)}
.dept--rnd{left:461px;top:400px;background-color:var(--c-rnd)}
.dept--ops{left:418px;top:498px;background-color:var(--c-ops)}
.dept--clinical{left:332px;top:560px;background-color:var(--c-clinical)}
.dept--quality{left:226px;top:566px;background-color:var(--c-quality)}
.dept--people{left:133px;top:520px;background-color:var(--c-people)}
.dept--marketing{left:77px;top:438px;background-color:var(--c-marketing)}
.dept--legal{left:70px;top:338px;background-color:var(--c-legal)}
.dept--access{left:110px;top:248px;background-color:var(--c-access);font-size:9px}

.month{position:absolute;width:112px}
.month__name{height:18px;background:var(--lunch-band);color:var(--white);font-size:15px;line-height:18px;text-align:center}
.month__week,.month__days{display:grid;grid-template-columns:repeat(7,1fr);text-align:center}
.month__week{height:8px;background:var(--lunch-sub);font-size:5.5px;line-height:8px;color:#7b7d80}
.month__week span:first-child{color:var(--sunday)}
.month__days{grid-auto-rows:9.6px;font-size:6.3px;line-height:9.6px;color:var(--ink);margin-top:1px}
.month__days > :nth-child(7n+1){color:var(--sunday)}
.month__days b{font-weight:400;background:var(--hl);margin:1px 3px}
.month__days i{font-style:normal}

.topics{position:absolute;left:18px;top:460px;width:488px;height:152px;border:3px solid var(--lunch-line);border-bottom:none;border-radius:26px 26px 0 0}
.topics__label{position:absolute;left:155px;top:446px;width:213px;height:28px;border-radius:14px;background:var(--lunch-line);color:var(--white);font-size:17px;font-weight:500;line-height:28px;text-align:center}
.topics__list{position:absolute;left:42px;top:478px;width:418px;list-style:none}
.topics__list li{display:flex;align-items:center;height:13.1px;font-size:10.6px;color:var(--ink)}
.topics__list .rule{flex:1;height:1px;background:#cfd1d3;margin:0 8px}
.topics__list .when{width:62px}
</style>
</head>
<body>

<section class="page page--breakfast">
  <h1 class="header"><span class="header__year">2018 CALENDAR</span><span class="header__sub">BREAKFAST BRIEFINGS</span></h1>

  <svg class="orbit" width="524" height="655" viewBox="0 0 524 655" aria-hidden="true">
    <circle cx="264" cy="372" r="201" fill="none" stroke="var(--orbit)" stroke-width="5"/>
    <circle cx="264" cy="372" r="154" fill="var(--orange-ring)"/>
  </svg>
  <div class="hero" role="img" aria-label="Photo of a tablet on a wooden desk showing the Corvane 2018 Calendar Breakfast Briefings title"></div>

  <div class="dept dept--tos">TOS<br>Dana Whitfield<br>December</div>
  <div class="dept dept--medical">Medical<br>Owen Marlowe<br>2019<br>TBD</div>
  <div class="dept dept--sales">Sales<br>Tom Ravell<br>2019<br>TBD</div>
  <div class="dept dept--finance">Finance<br>Sam Pellar<br>March</div>
  <div class="dept dept--rnd">R&amp;D<br>Nick<br>Andreadis<br>April</div>
  <div class="dept dept--ops">Operations<br>Lukas Brenner<br>May</div>
  <div class="dept dept--clinical">Clinical/ Reg<br>Evan Hollis<br>June</div>
  <div class="dept dept--quality">Quality<br>Martin<br>Kovalek<br>July</div>
  <div class="dept dept--people">People<br>Priya Menon<br>August</div>
  <div class="dept dept--marketing">Marketing<br>Rohan Batra<br>September</div>
  <div class="dept dept--legal">Legal<br>Imran Qadir<br>October</div>
  <div class="dept dept--access">Market Access<br>Helena<br>Vosberg<br>November</div>
</section>

<section class="page page--lunch">
  <h1 class="header"><span class="header__year">2018 CALENDAR</span><span class="header__sub">LUNCH &amp; LEARN</span></h1>

  <div class="month" style="left:18px;top:142px">
    <div class="month__name">January</div>
    <div class="month__week"><span>S</span><span>M</span><span>T</span><span>W</span><span>T</span><span>F</span><span>S</span></div>
    <div class="month__days"><i></i><span>1</span><span>2</span><span>3</span><span>4</span><span>5</span><span>6</span><span>7</span><span>8</span><span>9</span><span>10</span><span>11</span><span>12</span><span>13</span><span>14</span><span>15</span><span>16</span><span>17</span><b>18</b><span>19</span><span>20</span><span>21</span><span>22</span><span>23</span><span>24</span><span>25</span><span>26</span><span>27</span><span>28</span><span>29</span><span>30</span><span>31</span></div>
  </div>
  <div class="month" style="left:142px;top:142px">
    <div class="month__name">FEBRUARY</div>
    <div class="month__week"><span>S</span><span>M</span><span>T</span><span>W</span><span>T</span><span>F</span><span>S</span></div>
    <div class="month__days"><i></i><i></i><i></i><i></i><span>1</span><span>2</span><span>3</span><span>4</span><span>5</span><span>6</span><span>7</span><span>8</span><span>9</span><span>10</span><span>11</span><span>12</span><span>13</span><span>14</span><span>15</span><span>16</span><span>17</span><span>18</span><span>19</span><b>20</b><span>21</span><span>22</span><span>23</span><span>24</span><span>25</span><b>26</b><span>27</span><span>28</span></div>
  </div>
  <div class="month" style="left:268px;top:142px">
    <div class="month__name">MARCH</div>
    <div class="month__week"><span>S</span><span>M</span><span>T</span><span>W</span><span>T</span><span>F</span><span>S</span></div>
    <div class="month__days"><i></i><i></i><i></i><i></i><span>1</span><b>2</b><span>3</span><span>4</span><span>5</span><span>6</span><span>7</span><span>8</span><b>9</b><span>10</span><span>11</span><span>12</span><span>13</span><span>14</span><span>15</span><b>16</b><span>17</span><span>18</span><span>19</span><span>20</span><span>21</span><b>22</b><b>23</b><span>24</span><span>25</span><span>26</span><span>27</span><span>28</span><b>29</b><span>30</span><span>31</span></div>
  </div>
  <div class="month" style="left:394px;top:142px">
    <div class="month__name">April</div>
    <div class="month__week"><span>S</span><span>M</span><span>T</span><span>W</span><span>T</span><span>F</span><span>S</span></div>
    <div class="month__days"><span>1</span><span>2</span><span>3</span><span>4</span><span>5</span><b>6</b><span>7</span><span>8</span><span>9</span><span>10</span><span>11</span><span>12</span><b>13</b><span>14</span><span>15</span><span>16</span><span>17</span><span>18</span><span>19</span><span>20</span><span>21</span><span>22</span><span>23</span><span>24</span><span>25</span><b>26</b><b>27</b><span>28</span><span>29</span><span>30</span></div>
  </div>

  <div class="month" style="left:18px;top:234px">
    <div class="month__name">May</div>
    <div class="month__week"><span>S</span><span>M</span><span>T</span><span>W</span><span>T</span><span>F</span><span>S</span></div>
    <div class="month__days"><i></i><i></i><span>1</span><span>2</span><span>3</span><b>4</b><span>5</span><span>6</span><span>7</span><span>8</span><span>9</span><span>10</span><b>11</b><span>12</span><span>13</span><span>14</span><b>15</b><span>16</span><span>17</span><b>18</b><span>19</span><span>20</span><span>21</span><span>22</span><span>23</span><span>24</span><b>25</b><span>26</span><span>27</span><b>28</b><span>29</span><span>30</span><span>31</span></div>
  </div>
  <div class="month" style="left:142px;top:234px">
    <div class="month__name">June</div>
    <div class="month__week"><span>S</span><span>M</span><span>T</span><span>W</span><span>T</span><span>F</span><span>S</span></div>
    <div class="month__days"><i></i><i></i><i></i><i></i><i></i><b>1</b><span>2</span><span>3</span><span>4</span><span>5</span><span>6</span><span>7</span><b>8</b><span>9</span><span>10</span><span>11</span><span>12</span><span>13</span><span>14</span><b>15</b><span>16</span><span>17</span><span>18</span><span>19</span><span>20</span><span>21</span><b>22</b><span>23</span><span>24</span><span>25</span><span>26</span><span>27</span><span>28</span><b>29</b><span>30</span></div>
  </div>
  <div class="month" style="left:268px;top:234px">
    <div class="month__name">July</div>
    <div class="month__week"><span>S</span><span>M</span><span>T</span><span>W</span><span>T</span><span>F</span><span>S</span></div>
    <div class="month__days"><span>1</span><span>2</span><span>3</span><b>4</b><span>5</span><span>6</span><span>7</span><span>8</span><span>9</span><span>10</span><span>11</span><span>12</span><span>13</span><span>14</span><span>15</span><span>16</span><span>17</span><b>18</b><span>19</span><span>20</span><span>21</span><span>22</span><span>23</span><span>24</span><span>25</span><span>26</span><span>27</span><span>28</span><span>29</span><span>30</span><span>31</span></div>
  </div>
  <div class="month" style="left:394px;top:234px">
    <div class="month__name">August</div>
    <div class="month__week"><span>S</span><span>M</span><span>T</span><span>W</span><span>T</span><span>F</span><span>S</span></div>
    <div class="month__days"><i></i><i></i><i></i><span>1</span><span>2</span><b>3</b><span>4</span><span>5</span><span>6</span><span>7</span><span>8</span><span>9</span><b>10</b><span>11</span><span>12</span><span>13</span><span>14</span><span>15</span><span>16</span><span>17</span><span>18</span><span>19</span><span>20</span><span>21</span><span>22</span><span>23</span><span>24</span><span>25</span><span>26</span><span>27</span><span>28</span><span>29</span><span>30</span><span>31</span></div>
  </div>

  <div class="month" style="left:18px;top:326px">
    <div class="month__name">September</div>
    <div class="month__week"><span>S</span><span>M</span><span>T</span><span>W</span><span>T</span><span>F</span><span>S</span></div>
    <div class="month__days"><i></i><i></i><i></i><i></i><i></i><i></i><span>1</span><span>2</span><b>3</b><span>4</span><span>5</span><span>6</span><span>7</span><span>8</span><span>9</span><span>10</span><span>11</span><span>12</span><span>13</span><span>14</span><span>15</span><span>16</span><span>17</span><span>18</span><span>19</span><span>20</span><span>21</span><span>22</span><span>23</span><span>24</span><span>25</span><span>26</span><span>27</span><span>28</span><span>29</span><span>30</span></div>
  </div>
  <div class="month" style="left:142px;top:326px">
    <div class="month__name">October</div>
    <div class="month__week"><span>S</span><span>M</span><span>T</span><span>W</span><span>T</span><span>F</span><span>S</span></div>
    <div class="month__days"><i></i><span>1</span><span>2</span><span>3</span><span>4</span><span>5</span><span>6</span><span>7</span><span>8</span><span>9</span><span>10</span><span>11</span><span>12</span><span>13</span><span>14</span><span>15</span><span>16</span><span>17</span><span>18</span><span>19</span><span>20</span><span>21</span><span>22</span><span>23</span><span>24</span><span>25</span><span>26</span><span>27</span><span>28</span><span>29</span><span>30</span><span>31</span></div>
  </div>
  <div class="month" style="left:268px;top:326px">
    <div class="month__name">November</div>
    <div class="month__week"><span>S</span><span>M</span><span>T</span><span>W</span><span>T</span><span>F</span><span>S</span></div>
    <div class="month__days"><i></i><i></i><i></i><i></i><span>1</span><span>2</span><span>3</span><span>4</span><span>5</span><span>6</span><span>7</span><span>8</span><span>9</span><span>10</span><span>11</span><span>12</span><span>13</span><span>14</span><span>15</span><span>16</span><span>17</span><span>18</span><span>19</span><span>20</span><span>21</span><span>22</span><span>23</span><span>24</span><span>25</span><span>26</span><span>27</span><b>28</b><b>29</b><span>30</span></div>
  </div>
  <div class="month" style="left:394px;top:326px">
    <div class="month__name">December</div>
    <div class="month__week"><span>S</span><span>M</span><span>T</span><span>W</span><span>T</span><span>F</span><span>S</span></div>
    <div class="month__days"><i></i><i></i><i></i><i></i><i></i><i></i><span>1</span><span>2</span><span>3</span><span>4</span><span>5</span><span>6</span><span>7</span><span>8</span><span>9</span><span>10</span><span>11</span><span>12</span><span>13</span><span>14</span><span>15</span><span>16</span><span>17</span><span>18</span><span>19</span><span>20</span><span>21</span><span>22</span><span>23</span><b>24</b><b>25</b><b>26</b><span>27</span><span>28</span><span>29</span><span>30</span><b>31</b></div>
  </div>

  <div class="topics"></div>
  <h2 class="topics__label">Lunch &amp; Learn</h2>
  <ul class="topics__list">
    <li><span>Mindfulness</span><span class="rule"></span><span class="when">March</span></li>
    <li><span>Nutrition and Lifestyle Coaching</span><span class="rule"></span><span class="when">April</span></li>
    <li><span>What is Neuromodulation?</span><span class="rule"></span><span class="when">May</span></li>
    <li><span>Achieve Your Goals</span><span class="rule"></span><span class="when">June</span></li>
    <li><span>Changing Your Life with Positive Thinking</span><span class="rule"></span><span class="when">July</span></li>
    <li><span>What is Clean Eating and How Do I Get Started</span><span class="rule"></span><span class="when">August</span></li>
    <li><span>Budgeting 101 Financial Wellness</span><span class="rule"></span><span class="when">September</span></li>
    <li><span>Busted! Nutrition Myths</span><span class="rule"></span><span class="when">October</span></li>
    <li><span>Time Management: No time like the present</span><span class="rule"></span><span class="when">November</span></li>
    <li><span>1st Time Home Buyers</span><span class="rule"></span><span class="when">December</span></li>
  </ul>
</section>

</body>
</html>
```